Exclusive Furniture Company
Relunda GmbH
Project: Exclusive Furniture Company
Exclusive Furniture Company - General Merchandise
Creative Brief
Professional
Tarin HOLDEVA
CEO
Wolkenriedstrasse 4 8124 Lindwiler - Zürich Switzerland
t.tarin@relunda.ch
www.relunda.ch
Only the symbol R from Logo
Sarah2014 Sarah2014
Dear Designers I need Business Card and Stationary! (not only Business Cards) Thanks in advance Greta
Dear Designer, Please try the black color in other color variants... Thanks in advance! Greta
Dear Designer, Back of the business card is OK Fron part only with logo! see atachemnt: http://relunda.ch/logo/business-card-relunda.png Thanks in advance! Greta PS: I apologize for my English mistakes.

```html
<!DOCTYPE html>
<html lang="en">
<head>
<meta charset="utf-8">
<title>Relunda GmbH – Business Card</title>
<link rel="stylesheet" href="https://fonts.googleapis.com/css2?family=Arimo:wght@400;700&display=swap">
<style>
  :root {
    --backdrop: #262626;
    --card-white: #f4f4f4;
    --brand-red: #d81f27;
    --brand-red-deep: #9c0f16;
    --swoosh-grey: #3a3a3a;
    --ink-dark: #3b3b3b;
    --name-maroon: #5a070c;
    --on-red: #ffffff;
  }
  * { margin: 0; padding: 0; box-sizing: border-box; }
  html, body { width: 1200px; height: 820px; overflow: hidden; }
  body {
    background: var(--backdrop);
    font-family: "Arimo", Arial, sans-serif;
    position: relative;
  }
  .card {
    position: absolute;
    top: 255px;
    width: 540px;
    height: 310px;
    border-radius: 18px;
    background: var(--card-white);
    overflow: hidden;
    box-shadow: 0 10px 28px rgba(0,0,0,.45);
  }
  .card--front { left: 40px; }
  .card--back { left: 620px; }

  .wordmark {
    display: flex;
    align-items: center;
    gap: 14px;
    font-weight: 700;
    color: var(--ink-dark);
    letter-spacing: 3px;
  }
  .wordmark__square {
    background: var(--brand-red);
    flex: none;
  }
  .card--front .wordmark {
    position: absolute;
    left: 50%; top: 50%;
    transform: translate(-50%, -50%);
    font-size: 54px;
  }
  .card--front .wordmark__square { width: 52px; height: 52px; }

  .card__art { position: absolute; inset: 0; }
  .card--back .wordmark {
    position: absolute;
    left: 40px; top: 78px;
    font-size: 34px;
    gap: 10px;
  }
  .card--back .wordmark__square { width: 34px; height: 34px; }

  .contact {
    position: absolute;
    right: 30px; top: 40px;
    text-align: right;
    color: var(--on-red);
    font-size: 13px;
    line-height: 1.35;
  }
  .contact__name { color: var(--name-maroon); font-size: 20px; font-weight: 400; }
  .contact__title { color: var(--ink-dark); font-size: 14px; margin-bottom: 20px; }
  .contact__address { margin-bottom: 18px; }
  .contact__line { display: flex; justify-content: flex-end; align-items: center; gap: 6px; }
  .contact__icon { width: 11px; height: 11px; flex: none; }
</style>
</head>
<body>

<section class="card card--front" aria-label="Business card front">
  <div class="wordmark"><span class="wordmark__square"></span>RELUNDA</div>
</section>

<section class="card card--back" aria-label="Business card back">
  <svg class="card__art" viewBox="0 0 540 310" width="540" height="310" aria-hidden="true">
    <defs>
      <radialGradient id="redField" cx="0.7" cy="0.55" r="0.7">
        <stop offset="0" stop-color="#e8232c"/>
        <stop offset="1" stop-color="#a3111a"/>
      </radialGradient>
    </defs>
    <path d="M318,0 C238,45 316,185 160,224 C95,240 40,244 0,248 L0,310 L540,310 L540,0 Z" fill="var(--swoosh-grey)"/>
    <path d="M336,0 C258,48 336,196 176,236 C110,252 50,256 0,260 L0,310 L540,310 L540,0 Z" fill="url(#redField)"/>
  </svg>

  <div class="wordmark"><span class="wordmark__square"></span>RELUNDA</div>

  <div class="contact">
    <p class="contact__name">Marek Linden</p>
    <p class="contact__title">Director General</p>
    <p class="contact__address">Suite # 118, Oak<br>Bldg, NY 40217</p>
    <p class="contact__line">727 310.482
      <svg class="contact__icon" viewBox="0 0 12 12"><rect x="1" y="4" width="10" height="6" rx="1" fill="var(--ink-dark)"/><rect x="3" y="2" width="6" height="3" rx="1" fill="var(--ink-dark)"/></svg></p>
    <p class="contact__line">305-418-2076
      <svg class="contact__icon" viewBox="0 0 12 12"><rect x="3" y="0.5" width="6" height="11" rx="1.2" fill="var(--ink-dark)"/></svg></p>
    <p class="contact__line">hello@lindenmail.com
      <svg class="contact__icon" viewBox="0 0 12 12"><rect x="0.5" y="2" width="11" height="8" rx="1" fill="var(--ink-dark)"/><path d="M1 2.5 L6 7 L11 2.5" stroke="#ffffff" stroke-width="1" fill="none"/></svg></p>
    <p class="contact__line">www.lindenstudio.com
      <svg class="contact__icon" viewBox="0 0 12 12"><circle cx="6" cy="6" r="5" fill="none" stroke="var(--ink-dark)" stroke-width="1.4"/><path d="M1 6 H11 M6 1 C3 4 3 8 6 11 C9 8 9 4 6 1" fill="none" stroke="var(--ink-dark)" stroke-width="1"/></svg></p>
  </div>
</section>

</body>
</html>
```